Create Premium Wine Label Design

We are premium wine exporters from Australia. We are looking to introduce new brand " The Velloro" - in red wine, White wine and Sparkling wine to international market.

The sample label design for red wine ( Shiraz) is attached.

This is our luxury brand. We need a stunning wine label designs for (front, back and neck) that should be mostly in GOLD colour and design should be really eye catching.

We have provided sample design for front, back and neck labels. However, we are looking forward to see a completely new improvised design.

LOGO attached.

Front Label Design Specification:

* We would like to see designs that are in Gold colour.
* Wine Bottle size is standard: 750ml; we assume the same design can be resizable to different bottle sizes.
* Our design should suit both black, white and sparkling wine bottles(sample attached)
* Use our logo in the design (see attached - label sample)
* Content for front label (see attached).
* Design should include all information specified in the sample

Back Label Design
* All contents in the sample should be used ( sample attached)
* LOGO attached.

Neck Label Design
* Sample of Neck label attached, please provide similar or your own design.
* LOGO attached.

Image Samples:
* Samples of label designs we like (see attached)
* Sample for gold color (see attached)
* For bottle shapes (see attached)
* Front, Back and Neck Label Samples (see attached)

Target Market(s)

International Wine Market

Font styles to use
Decorative
Script

Requirements
Must have
• Must have golden color on front and back label

```html
<!DOCTYPE html>
<html lang="en">
<head>
<meta charset="utf-8">
<title>The Velloro Shiraz – Front Label</title>
<link rel="stylesheet" href="https://fonts.googleapis.com/css2?family=Source+Sans+3:wght@400;600;700&family=Yellowtail&display=swap">
<style>
  :root {
    --canvas: #ffffff;
    --label-black: #050505;
    --gold: #f5c518;
    --gold-soft: #f9de6a;
    --gold-pale: #fbeaa6;
    --white: #ffffff;
    --ink: #111111;
  }
  * { margin: 0; padding: 0; box-sizing: border-box; }
  html, body {
    width: 1200px;
    height: 975px;
    overflow: hidden;
    background: var(--canvas);
  }
  .canvas {
    position: relative;
    width: 1200px;
    height: 975px;
  }
  .front-label {
    position: absolute;
    left: 308px;
    top: 78px;
    width: 583px;
    height: 818px;
  }
  .label-border-texture {
    position: absolute;
    inset: 0;
    background: radial-gradient(circle at 50% 50%, var(--gold-soft), var(--gold-pale));
  }
  .label-panel {
    position: absolute;
    inset: 26px;
    background: var(--label-black);
  }
  .label-frame {
    position: absolute;
    inset: 13px;
    border: 2px solid var(--gold);
  }
  .brand {
    position: absolute;
    top: 130px;
    left: 0;
    right: 0;
    display: flex;
    justify-content: center;
    align-items: center;
    gap: 10px;
  }
  .brand-dot {
    width: 14px;
    height: 14px;
    border-radius: 50%;
    background: var(--gold);
  }
  .brand-name {
    font-family: "Source Sans 3", sans-serif;
    font-weight: 600;
    font-size: 26px;
    letter-spacing: 1px;
    color: var(--gold);
    text-transform: uppercase;
  }
  .flourish {
    position: absolute;
    left: 106px;
    width: 319px;
    height: 52px;
    background: linear-gradient(90deg, rgba(245,197,24,0), rgba(245,197,24,0.55) 30%, rgba(245,197,24,0.55) 70%, rgba(245,197,24,0));
    border-radius: 26px;
  }
  .flourish-top { top: 205px; }
  .flourish-bottom { top: 350px; }
  .wine-name {
    position: absolute;
    top: 268px;
    left: 0;
    right: 0;
    text-align: center;
    font-family: "Yellowtail", cursive;
    font-size: 70px;
    line-height: 1;
    color: var(--gold);
  }
  .varietal {
    position: absolute;
    top: 518px;
    left: 0;
    right: 0;
    text-align: center;
    font-family: "Source Sans 3", sans-serif;
    font-weight: 700;
    font-size: 31px;
    letter-spacing: 1px;
    color: var(--white);
  }
  .vintage {
    position: absolute;
    top: 580px;
    left: 0;
    right: 0;
    text-align: center;
    font-family: "Source Sans 3", sans-serif;
    font-weight: 400;
    font-size: 27px;
    color: var(--white);
  }
  .origin-band {
    position: absolute;
    left: 99px;
    top: 703px;
    width: 330px;
    height: 34px;
    background: var(--gold);
    display: flex;
    align-items: center;
    justify-content: center;
    font-family: "Source Sans 3", sans-serif;
    font-weight: 400;
    font-size: 19px;
    color: var(--ink);
    text-transform: uppercase;
  }
</style>
</head>
<body>
  <main class="canvas">
    <section class="front-label">
      <div class="label-border-texture" role="img" aria-label="Speckled gold texture border"></div>
      <div class="label-panel">
        <div class="label-frame"></div>
        <div class="brand">
          <span class="brand-dot"></span>
          <span class="brand-name">Corvella</span>
        </div>
        <div class="flourish flourish-top" role="img" aria-label="Gold ornamental flourish above the wine name"></div>
        <h1 class="wine-name">The Velloro</h1>
        <div class="flourish flourish-bottom" role="img" aria-label="Gold ornamental flourish below the wine name"></div>
        <p class="varietal">SHIRAZ</p>
        <p class="vintage">2018</p>
        <p class="origin-band">Wine of Australia</p>
      </div>
    </section>
  </main>
</body>
</html>
```